Vape case graphic design

We are looking to create unique design with pattern prints for our Vape case.

The appearance is required to be dynamic and layered, also our theme is related to ice, we need the ice feeling. And we need the design which is matched with European and America style.

We attached our Vape case size and shape for your reference. Pls put your design on the vape case, not just give us the plain design artwork.

Target Market(s)

European and American market

Industry/Entity Type

Vape

```html
<!DOCTYPE html>
<html lang="en">
<head>
<meta charset="UTF-8">
<title>Vape Case – Ice Edition</title>
<link href="https://fonts.googleapis.com/css2?family=Montserrat:wght@600;700;800&display=swap" rel="stylesheet">
<style>
  :root {
    --canvas-bg: #ffffff;
    --ice-deep: #2c6f9f;
    --ice-mid: #78b3d6;
    --ice-light: #d4e9f4;
    --ice-glow: #eef7fc;
    --text-white: #ffffff;
    --text-navy: #0f3a5c;
    --cap-silver: #e9ecef;
    --cap-shade: #b9c0c7;
    --cap-dark: #2a2f36;
  }
  * { margin: 0; padding: 0; box-sizing: border-box; }
  html, body {
    width: 800px;
    height: 1200px;
    overflow: hidden;
    background: var(--canvas-bg);
    font-family: "Montserrat", sans-serif;
  }
  .artboard {
    position: relative;
    width: 800px;
    height: 1200px;
  }
  .case-art {
    position: absolute;
    left: 0;
    top: 0;
    width: 800px;
    height: 620px;
  }
  .case-title {
    position: absolute;
    left: 291px;
    top: 194px;
    font-weight: 800;
    font-size: 33px;
    line-height: 34px;
    letter-spacing: 0.5px;
  }
  .case-title .line-light { color: var(--text-white); display: block; }
  .case-title .line-dark { color: var(--text-navy); display: block; }
  .case-tagline {
    position: absolute;
    left: 291px;
    top: 285px;
    writing-mode: vertical-rl;
    font-weight: 700;
    font-size: 14px;
    letter-spacing: 5.2px;
    color: var(--text-white);
  }
  .case-volume {
    position: absolute;
    left: 455px;
    top: 527px;
    font-weight: 600;
    font-size: 13px;
    letter-spacing: 0.5px;
    color: var(--text-white);
  }
  .pattern-panel {
    position: absolute;
    left: 0;
    top: 710px;
    width: 800px;
    height: 490px;
    background:
      radial-gradient(ellipse 40% 45% at 50% 45%, var(--ice-glow) 0%, rgba(238,247,252,0) 70%),
      radial-gradient(ellipse 30% 30% at 12% 20%, rgba(44,111,159,0.55) 0%, rgba(44,111,159,0) 70%),
      radial-gradient(ellipse 25% 35% at 85% 25%, rgba(44,111,159,0.5) 0%, rgba(44,111,159,0) 70%),
      radial-gradient(ellipse 35% 30% at 20% 90%, rgba(44,111,159,0.45) 0%, rgba(44,111,159,0) 70%),
      linear-gradient(180deg, var(--ice-mid) 0%, var(--ice-light) 45%, var(--ice-mid) 100%);
  }
</style>
</head>
<body>
<main class="artboard">
  <svg class="case-art" viewBox="0 0 800 620" xmlns="http://www.w3.org/2000/svg">
    <defs>
      <clipPath id="case-outline">
        <path d="M300,102 H390 Q397,102 397,110 V140 Q397,150 407,150 H498 Q520,150 520,172 V548 Q520,572 496,572 H289 Q265,572 265,548 V172 Q265,150 283,150 Q293,150 293,140 V110 Q293,102 300,102 Z"/>
      </clipPath>
      <linearGradient id="ice-base" x1="0" y1="0" x2="1" y2="1">
        <stop offset="0" stop-color="#3a7cab"/>
        <stop offset="0.45" stop-color="#a9d1e8"/>
        <stop offset="0.75" stop-color="#cfe6f3"/>
        <stop offset="1" stop-color="#4f93c2"/>
      </linearGradient>
      <radialGradient id="ice-glow" cx="0.6" cy="0.45" r="0.5">
        <stop offset="0" stop-color="#eef7fc" stop-opacity="0.85"/>
        <stop offset="1" stop-color="#eef7fc" stop-opacity="0"/>
      </radialGradient>
      <linearGradient id="cap-metal" x1="0" y1="0" x2="1" y2="0">
        <stop offset="0" stop-color="#b9c0c7"/>
        <stop offset="0.5" stop-color="#f4f6f8"/>
        <stop offset="1" stop-color="#b9c0c7"/>
      </linearGradient>
      <filter id="case-shadow" x="-20%" y="-20%" width="140%" height="140%">
        <feDropShadow dx="0" dy="3" stdDeviation="5" flood-color="#000" flood-opacity="0.12"/>
      </filter>
    </defs>

    <g class="mouthpiece">
      <rect x="296" y="80" width="98" height="26" rx="4" fill="url(#cap-metal)"/>
      <path d="M322,84 H368 L352,100 H338 Z" fill="var(--cap-dark)"/>
    </g>

    <g class="case-body" filter="url(#case-shadow)">
      <g clip-path="url(#case-outline)" role="img" aria-label="Close-up photograph of crushed blue ice crystals covering the case">
        <rect x="260" y="95" width="265" height="480" fill="url(#ice-base)"/>
        <rect x="260" y="95" width="265" height="480" fill="url(#ice-glow)"/>
      </g>
    </g>
  </svg>

  <h1 class="case-title">
    <span class="line-light">LOREM</span>
    <span class="line-dark">IPSUM</span>
  </h1>
  <p class="case-tagline">DOLOR SIT AMET</p>
  <p class="case-volume">10ML</p>

  <div class="pattern-panel" role="img" aria-label="Full ice crystal pattern artwork in light and deep blue tones"></div>
</main>
</body>
</html>
```